Ridgeline Orchards Organic Cherry POS card 7x11

We are wanting to create a one-sided 7 x 11 organic cherry card that is eye catching and informative.This should be clear and easy to read and not cluttered. We use these cards as a display in grocery stores, demo stands, and other events to market Organic Ridgeline Sweet Orchards. We have a few facts that we would like displayed on the card (see attachment).

Target Market(s)

Consumers

Industry/Entity Type

Agriculture

Requirements
Must have
• Natural color palettes
• Easy to read
• Ridgeline Orchards
Nice to have
• Unique, realistic cherry design

```html
<!DOCTYPE html>
<html lang="en">
<head>
<meta charset="UTF-8">
<title>Ridgeline Orchards – Organic Sweet Cherries Card</title>
<link href="https://fonts.googleapis.com/css2?family=Cabin:ital,wght@0,500;1,500;1,600&family=Source+Sans+3:wght@400&display=swap" rel="stylesheet">
<style>
  :root {
    --paper: #ffffff;
    --paper-shade: #ececeb;
    --cherry: #c8182a;
    --cherry-deep: #8e0f1b;
    --cherry-dark: #6d0a14;
    --leaf: #6aab2e;
    --leaf-dark: #2e8b3d;
    --tick: #3aa648;
    --text-brown: #5a4a42;
    --text-grey: #555555;
    --ink: #2a2a2a;
    --straw: #c9a46a;
    --straw-dark: #a9824a;
  }
  * { box-sizing: border-box; margin: 0; padding: 0; }
  html, body { width: 1200px; height: 856px; overflow: hidden; background: var(--paper); }
  .card {
    position: relative;
    width: 1200px;
    height: 856px;
    overflow: hidden;
    background: linear-gradient(180deg, var(--paper) 0%, #f7f7f6 55%, var(--paper-shade) 100%);
    font-family: "Source Sans 3", sans-serif;
  }

  .brand {
    position: absolute;
    left: 56px;
    top: 86px;
    display: flex;
    align-items: center;
    gap: 18px;
  }
  .brand-dot {
    width: 58px; height: 58px;
    border-radius: 50%;
    background: var(--cherry-deep);
  }
  .brand-name {
    font-family: "Cabin", sans-serif;
    font-weight: 500;
    font-size: 54px;
    color: var(--ink);
    letter-spacing: 0.5px;
  }

  .hero-photo {
    position: absolute;
    left: 0; top: 210px;
    width: 760px; height: 646px;
    background:
      radial-gradient(ellipse 34% 30% at 44% 30%, rgba(160,18,34,0.85) 0%, rgba(180,30,45,0.55) 45%, rgba(255,255,255,0) 100%),
      radial-gradient(ellipse 42% 40% at 42% 48%, #f4f4f4 0%, #e9e9e8 60%, rgba(255,255,255,0) 100%),
      radial-gradient(ellipse 24% 18% at 78% 62%, rgba(140,20,35,0.6) 0%, rgba(255,255,255,0) 100%);
  }

  .tagline {
    position: absolute;
    left: 664px; top: 68px;
    width: 530px;
    text-align: center;
    font-family: "Cabin", sans-serif;
    font-style: italic;
    font-weight: 600;
    font-size: 34px;
    line-height: 56px;
    color: var(--text-brown);
  }

  .ribbon {
    position: absolute;
    left: 662px; top: 216px;
    width: 538px; height: 108px;
    background: linear-gradient(90deg, var(--cherry) 0%, #b5152a 55%, var(--cherry-deep) 100%);
    box-shadow: 0 4px 6px rgba(0,0,0,0.18);
    display: flex;
    align-items: center;
    padding-left: 20px;
  }
  .ribbon-fold {
    position: absolute;
    left: 662px; top: 194px;
    width: 0; height: 0;
    border-left: 9px solid transparent;
    border-bottom: 22px solid var(--cherry-dark);
  }
  .ribbon-title {
    color: #fff;
    font-size: 43px;
    font-weight: 400;
    letter-spacing: 0;
    white-space: nowrap;
  }

  .benefits {
    position: absolute;
    left: 726px; top: 364px;
    list-style: none;
  }
  .benefit {
    display: flex;
    align-items: center;
    gap: 18px;
    height: 56.5px;
    font-size: 33px;
    color: var(--text-grey);
    white-space: nowrap;
  }
  .benefit svg { width: 25px; height: 25px; flex: none; }

  .basket-photo {
    position: absolute;
    left: 1066px; top: 544px;
    width: 128px; height: 194px;
    border-radius: 40% 40% 30% 30%;
    background:
      radial-gradient(ellipse 45% 20% at 50% 44%, #b0142a 0%, rgba(176,20,42,0.6) 60%, rgba(201,164,106,0) 100%),
      linear-gradient(180deg, rgba(201,164,106,0) 0%, var(--straw) 48%, var(--straw-dark) 100%);
  }

  .wave { position: absolute; left: 0; top: 0; }

  .organic-seal {
    position: absolute;
    left: 22px; top: 636px;
    width: 126px; height: 126px;
    border-radius: 50%;
    background: var(--leaf-dark);
    opacity: 0.9;
  }

  .footnote {
    position: absolute;
    left: 700px; top: 754px;
    width: 460px;
    text-align: center;
    font-family: "Cabin", sans-serif;
    font-style: italic;
    font-weight: 500;
    font-size: 25px;
    line-height: 34px;
    color: #fff;
  }
</style>
</head>
<body>
<main class="card">
  <div class="hero-photo" role="img" aria-label="Photo of fresh red sweet cherries in a white colander, with loose cherries on a white table"></div>

  <div class="brand">
    <span class="brand-dot"></span>
    <span class="brand-name">Ridgeline Orchards</span>
  </div>

  <p class="tagline">Organic Ridgeline cherries make up<br>1/3 of the nation’s production.</p>

  <div class="ribbon-fold"></div>
  <div class="ribbon"><h1 class="ribbon-title">ORGANIC SWEET CHERRIES</h1></div>

  <ul class="benefits">
    <li class="benefit"><svg viewBox="0 0 26 26"><circle cx="13" cy="13" r="13" fill="var(--tick)"/><path d="M7 13.5l4 4 8-8" fill="none" stroke="#fff" stroke-width="3" stroke-linecap="round" stroke-linejoin="round"/></svg>Fat Free</li>
    <li class="benefit"><svg viewBox="0 0 26 26"><circle cx="13" cy="13" r="13" fill="var(--tick)"/><path d="M7 13.5l4 4 8-8" fill="none" stroke="#fff" stroke-width="3" stroke-linecap="round" stroke-linejoin="round"/></svg>Source of Vitamin C</li>
    <li class="benefit"><svg viewBox="0 0 26 26"><circle cx="13" cy="13" r="13" fill="var(--tick)"/><path d="M7 13.5l4 4 8-8" fill="none" stroke="#fff" stroke-width="3" stroke-linecap="round" stroke-linejoin="round"/></svg>A Natural Anti-Inflammatory</li>
    <li class="benefit"><svg viewBox="0 0 26 26"><circle cx="13" cy="13" r="13" fill="var(--tick)"/><path d="M7 13.5l4 4 8-8" fill="none" stroke="#fff" stroke-width="3" stroke-linecap="round" stroke-linejoin="round"/></svg>Source of Potassium</li>
    <li class="benefit"><svg viewBox="0 0 26 26"><circle cx="13" cy="13" r="13" fill="var(--tick)"/><path d="M7 13.5l4 4 8-8" fill="none" stroke="#fff" stroke-width="3" stroke-linecap="round" stroke-linejoin="round"/></svg>Source of Melatonin</li>
  </ul>

  <svg class="wave" width="1200" height="856" viewBox="0 0 1200 856" aria-hidden="true">
    <defs>
      <linearGradient id="bandFill" x1="0" y1="0" x2="1" y2="0">
        <stop offset="0" stop-color="#c8182a"/>
        <stop offset="0.6" stop-color="#a8111f"/>
        <stop offset="1" stop-color="#8e0f1b"/>
      </linearGradient>
    </defs>
    <path d="M0 770 C 300 790, 520 700, 760 676 C 950 658, 1080 660, 1200 692 L1200 716 C 1080 690, 940 690, 760 706 C 520 730, 300 800, 0 782 Z" fill="#ffffff"/>
    <path d="M0 770 C 300 790, 520 700, 760 676 C 950 658, 1080 660, 1200 692" fill="none" stroke="var(--leaf)" stroke-width="7"/>
    <path d="M0 790 C 300 808, 520 735, 760 712 C 940 696, 1080 700, 1200 730 L1200 856 L0 856 Z" fill="url(#bandFill)"/>
  </svg>

  <div class="basket-photo" role="img" aria-label="Photo of a wicker basket filled with red cherries"></div>
  <div class="organic-seal" role="img" aria-label="Organic certification seal"></div>

  <p class="footnote">Washington State is the nation’s largest<br>producer of organic cherries.</p>
</main>
</body>
</html>
```